Business card for Industrial Automation Company.

The company is called Process and Signal Dynamics. We are a systems integration company in South Africa specializing in PLC and SCADA programming, systems integration and industrial automation. Attached find logo and cover letter of the company for a feel of the general look. The website is still under development, so you will have to use your own ideas.

Please blend the colors on the business card as per the logo colors. Must be clean, professional look. Please submit a creative professional design. If a background color is used please do not use dark colored backgrounds.

Target Market(s)

Mining

Industry/Entity Type

Engineering Consultant

Contact Information for Business Card

Gerrit van Dyk (NDip Electrical LC; BSc)
Director / Systems Engineer

Postal Address
PO Box 2867
Vredenburg
7380

Physical Address:
Kloofhoek Street 27
Vredenburg
7380

Tel: +22 548 6170
Cell: +27 82 953 4086
Mail: gerritv@psd-zx.com
Web: www.psd-zx.com

Font styles to use
Sans Serif

Colors

Designer to choose colors to be used in the design.

Requirements
Must have
• Backside of the card must also contain the following:
• Services
• *Industrial Automation
• *Control System design and configuration
• *Systems Integration
• *Equipment Supply
• Industries
• *Mining
• *Factory
• *Oil and Gas
Nice to have
• Colors must blend in with colors of logo. Not too much color and no dark backgrounds.
Should not have
• dark / black background. Preferably white / light background if any.

```html
<!DOCTYPE html>
<html lang="en">
<head>
<meta charset="utf-8">
<title>Process and Signal Dynamics – Business Card</title>
<link href="https://fonts.googleapis.com/css2?family=Arimo:wght@400;700&family=Open+Sans:wght@400;600&display=swap" rel="stylesheet">
<style>
  :root {
    --backdrop: #ece9e4;
    --card-front: #ebebeb;
    --brand-blue: #1c4384;
    --ink: #1e1e1e;
    --muted-grey: #6e6f72;
    --rule: #a9aaad;
    --back-top: #9b9da1;
    --back-bottom: #68696d;
    --back-text: #eef0f2;
    --accent-lime: #d6e22a;
  }
  * { box-sizing: border-box; margin: 0; padding: 0; }
  html, body { width: 1200px; height: 900px; overflow: hidden; }
  body {
    position: relative;
    background: var(--backdrop);
    font-family: "Arimo", Arial, sans-serif;
  }
  .card {
    position: absolute;
    box-shadow: 2px 3px 6px rgba(0,0,0,0.35);
  }
  .card-front {
    left: 320px; top: 88px; width: 580px; height: 357px;
    background: var(--card-front);
  }
  .card-back {
    left: 320px; top: 478px; width: 584px; height: 358px;
    background: linear-gradient(180deg, var(--back-top) 0%, var(--back-bottom) 100%);
    font-family: "Open Sans", Arial, sans-serif;
  }
  .brand {
    position: absolute; left: 40px; top: 38px;
    display: flex; align-items: center; gap: 14px;
    white-space: nowrap;
  }
  .brand-dot {
    width: 56px; height: 56px; border-radius: 50%;
    background: var(--brand-blue); flex: none;
  }
  .brand-name {
    font-weight: 700; font-size: 29px; line-height: 1;
    color: var(--brand-blue);
  }
  .tagline {
    position: absolute; left: 150px; top: 104px;
    font-size: 18px; letter-spacing: 1.1px; color: var(--muted-grey);
    white-space: nowrap;
  }
  .rule {
    position: absolute; left: 345px; top: 142px;
    width: 173px; height: 1px; background: var(--rule);
  }
  .person { position: absolute; left: 38px; top: 161px; }
  .person-name {
    font-weight: 700; font-size: 25px; color: var(--brand-blue);
    text-transform: uppercase; letter-spacing: 0.3px;
  }
  .person-credentials { font-size: 18px; color: var(--brand-blue); margin-top: 3px; }
  .person-title { font-size: 16px; color: var(--ink); margin-top: 4px; }
  .contact-list { list-style: none; margin-top: 12px; }
  .contact-list li {
    display: flex; align-items: center; gap: 5px;
    font-size: 16px; color: var(--ink); line-height: 21px;
  }
  .contact-list svg { width: 14px; height: 14px; fill: var(--brand-blue); flex: none; }
  .addresses {
    position: absolute; right: 30px; top: 188px; text-align: right;
  }
  .address-label { font-size: 18px; color: var(--brand-blue); }
  .address-line { font-size: 16px; color: var(--ink); line-height: 21px; }
  .address-block + .address-block { margin-top: 14px; }
  .back-section { position: absolute; left: 36px; }
  .services { top: 38px; }
  .industries { top: 219px; }
  .back-heading {
    font-weight: 600; font-size: 20px; color: var(--brand-blue);
    margin-bottom: 8px;
  }
  .back-list { list-style: none; }
  .back-list li {
    position: relative; padding-left: 15px;
    font-size: 15.8px; line-height: 21px; color: var(--back-text);
  }
  .back-list li::before {
    content: ""; position: absolute; left: 0; top: 7px;
    width: 8px; height: 8px; border-radius: 50%; background: var(--accent-lime);
  }
  .industries .back-list li { padding-left: 18px; }
</style>
</head>
<body>
  <section class="card card-front" aria-label="Business card front">
    <div class="brand">
      <span class="brand-dot"></span>
      <span class="brand-name">Process and Signal Dynamics</span>
    </div>
    <p class="tagline">Partnering for innovative solutions!</p>
    <div class="rule"></div>

    <div class="person">
      <h1 class="person-name">Gerrit van Dyk</h1>
      <p class="person-credentials">(NDip Electrical LC; BSc)</p>
      <p class="person-title">Director / Systems Engineer</p>
      <ul class="contact-list">
        <li><svg viewBox="0 0 16 16"><path d="M2 6c0-2 2-3 6-3s6 1 6 3l-3 1-1-2H6L5 7 2 6zm2 2h8l1 5H3l1-5zm4 1a1.5 1.5 0 100 3 1.5 1.5 0 000-3z"/></svg>+22 548 6170</li>
        <li><svg viewBox="0 0 16 16"><path d="M4 1h8v14H4V1zm1.5 1.5v9h5v-9h-5zM8 12.5a.8.8 0 100 1.6.8.8 0 000-1.6z"/></svg>+27 82 953 4086</li>
        <li><svg viewBox="0 0 16 16"><path d="M1 3h14v10H1V3zm1.5 1.5v.3L8 9l5.5-4.2v-.3h-11zm0 2.2v4.8h11V6.7L8 10.9 2.5 6.7z"/></svg>gerritv@psd-zx.com</li>
        <li><svg viewBox="0 0 16 16"><path d="M8 1a7 7 0 100 14A7 7 0 008 1zm-1 3l2 1-1 2 2 1 1 3-2 2-1-3-2-1V6L5 5l2-1z"/></svg>www.psd-zx.com</li>
      </ul>
    </div>

    <div class="addresses">
      <div class="address-block">
        <p class="address-label">Postal Address:</p>
        <p class="address-line">PO Box 2867</p>
        <p class="address-line">Soetmeer 7384</p>
      </div>
      <div class="address-block">
        <p class="address-label">Physical Address:</p>
        <p class="address-line">Kloofhoek Street 27</p>
        <p class="address-line">Soetmeer 7384</p>
      </div>
    </div>
  </section>

  <section class="card card-back" aria-label="Business card back">
    <div class="back-section services">
      <h2 class="back-heading">SERVICES</h2>
      <ul class="back-list">
        <li>Industrial Automation</li>
        <li>Control System design and configuration</li>
        <li>Systems Integration</li>
        <li>Equipment Supply</li>
      </ul>
    </div>
    <div class="back-section industries">
      <h2 class="back-heading">INDUSTRIES</h2>
      <ul class="back-list">
        <li>Mining</li>
        <li>Factory</li>
        <li>Oil and Gas</li>
      </ul>
    </div>
  </section>
</body>
</html>
```